roofing door hanger

we would like to have our logo kvt roofing, it would be given when we are working in the neighborhood and have our services roof replacement, roof repair, ventilation, inspections. Our slogan is "Reliability starts at the top" . Our company is kvt roofing i would like to get one or two reviews from google, and f any pictures are needed can use facebook.

Industry/Entity Type

Roofing

Requirements
Must have
• this has to be a door hanger design

```html
<!DOCTYPE html>
<html lang="en">
<head>
<meta charset="utf-8">
<title>KVT Roofing Door Hanger</title>
<link href="https://fonts.googleapis.com/css2?family=Barlow:wght@700;800&display=swap" rel="stylesheet">
<style>
  :root {
    --frame: #3b3b3d;
    --panel: #e6e7e8;
    --white: #ffffff;
    --orange: #f28321;
    --orange-deep: #c8561a;
    --ink: #3a3a3c;
    --grey-text: #5b5b5d;
  }
  html, body {
    margin: 0;
    padding: 0;
    width: 890px;
    height: 1200px;
    overflow: hidden;
    background: var(--frame);
    font-family: "Barlow", Arial, sans-serif;
  }
  .hanger {
    position: absolute;
    left: 72px;
    top: 72px;
    width: 747px;
    height: 1056px;
    background: var(--white);
    overflow: hidden;
  }
  .hanger-art {
    position: absolute;
    left: 0;
    top: 0;
  }
  .top-phone {
    position: absolute;
    left: 46px;
    top: 52px;
    margin: 0;
    font-size: 50px;
    font-weight: 700;
    color: var(--grey-text);
    letter-spacing: 0.5px;
  }
  .brand-name {
    position: absolute;
    left: 490px;
    top: 58px;
    width: 200px;
    margin: 0;
    font-size: 46px;
    line-height: 44px;
    font-weight: 800;
    color: var(--orange);
    text-align: center;
  }
  .slogan {
    position: absolute;
    left: 60px;
    top: 440px;
    margin: 0;
    font-size: 66px;
    line-height: 77px;
    font-weight: 800;
    color: var(--white);
    text-shadow: 3px 3px 0 rgba(40, 30, 25, 0.75);
    letter-spacing: -0.5px;
  }
  .services {
    position: absolute;
    left: 60px;
    top: 748px;
  }
  .services-title {
    margin: 0 0 6px;
    font-size: 35px;
    font-weight: 800;
    color: var(--ink);
  }
  .services-list {
    list-style: none;
    margin: 0;
    padding: 0;
  }
  .services-list li {
    position: relative;
    padding-left: 25px;
    font-size: 26px;
    line-height: 33px;
    font-weight: 700;
    color: var(--orange);
  }
  .services-list li::before {
    content: "";
    position: absolute;
    left: 3px;
    top: 11px;
    width: 11px;
    height: 11px;
    border-radius: 50%;
    background: var(--orange);
  }
  .footer-band {
    position: absolute;
    left: 0;
    top: 980px;
    width: 747px;
    height: 76px;
    background: var(--orange);
    color: var(--white);
    font-size: 35px;
    font-weight: 700;
    line-height: 76px;
    text-align: center;
    margin: 0;
  }
</style>
</head>
<body>
<main class="hanger">
  <svg class="hanger-art" width="747" height="1056" viewBox="0 0 747 1056" xmlns="http://www.w3.org/2000/svg">
    <defs>
      <linearGradient id="heroTone" x1="0" y1="0" x2="0.6" y2="1">
        <stop offset="0" stop-color="#e9883a"/>
        <stop offset="0.5" stop-color="#b8552a"/>
        <stop offset="1" stop-color="#8a3a1e"/>
      </linearGradient>
      <linearGradient id="thumbGrey" x1="0" y1="0" x2="1" y2="1">
        <stop offset="0" stop-color="#9aa0a6"/>
        <stop offset="1" stop-color="#3f4347"/>
      </linearGradient>
      <linearGradient id="thumbSteel" x1="0" y1="0" x2="0" y2="1">
        <stop offset="0" stop-color="#bcc3c9"/>
        <stop offset="1" stop-color="#6d7277"/>
      </linearGradient>
    </defs>
    <!-- upper light panel -->
    <rect class="top-panel" x="0" y="0" width="747" height="720" fill="var(--panel)"/>
    <!-- roofline stripe -->
    <polygon class="roof-stripe" points="0,292 228,140 747,300 747,322 228,162 0,314" fill="var(--orange)"/>
    <!-- hero photo area -->
    <g role="img" aria-label="Photo: two roofers laying shingles on a brick house roof under an orange sky">
      <polygon points="0,320 228,168 747,328 747,720 0,720" fill="var(--orange)"/>
      <polygon points="0,330 228,180 747,338 747,720 0,720" fill="url(#heroTone)"/>
    </g>
    <!-- white lower area -->
    <rect class="lower-panel" x="0" y="720" width="747" height="260" fill="var(--white)"/>
    <!-- thumbnails -->
    <g role="img" aria-label="Photo: gloved hand hammering a nail into roof shingles">
      <rect x="524" y="268" width="186" height="172" fill="var(--white)"/>
      <rect x="529" y="273" width="176" height="162" fill="url(#thumbGrey)"/>
    </g>
    <g role="img" aria-label="Photo: workers torching roll roofing on a flat roof">
      <rect x="524" y="452" width="186" height="150" fill="var(--white)"/>
      <rect x="529" y="457" width="176" height="140" fill="url(#thumbSteel)"/>
    </g>
    <g role="img" aria-label="Photo: hands fitting grey roof tiles onto battens">
      <rect x="524" y="616" width="186" height="148" fill="var(--white)"/>
      <rect x="527" y="619" width="180" height="145" fill="url(#thumbGrey)"/>
    </g>
    <g role="img" aria-label="Photo: gloved hands laying dark metal roof tiles">
      <rect x="527" y="782" width="180" height="146" fill="url(#thumbGrey)"/>
    </g>
    <!-- dark divider above footer -->
    <rect x="0" y="972" width="747" height="8" fill="var(--frame)"/>
  </svg>

  <p class="top-phone">716-555-0148</p>
  <p class="brand-name">KVT<br>ROOFING</p>

  <h1 class="slogan">RELIABILITY<br>STARTS AT<br>THE TOP</h1>

  <section class="services">
    <h2 class="services-title">OUR SERVICES:</h2>
    <ul class="services-list">
      <li>ROOF REPLACEMENT</li>
      <li>ROOF REPAIR</li>
      <li>VENTILATION</li>
      <li>INSPECTIONS</li>
    </ul>
  </section>

  <p class="footer-band">KVT-ROOFING.COM | 716-555-0148</p>
</main>
</body>
</html>
```